Website to showcase Pram Dash Days that will be held in Woodland Trustees areas in the UK

Looking for a website, designed in WordPress, to provide information on family orientated running events that I'm organising in the UK (I've registered the website address pramdashdays.co.uk). Refer to the Project Brief document however as a summary:
These events are unique, as they are for people running with a child in a buggy (or in a wheelchair) and will be on carefully designed, traffic-free courses in Woodland Trustees areas. The events, by using a specialist timing system, will allow runners to start within a two hour window therefore removing the anxiety / rush to get to the start line for the mass start. All events will be centred around a family day with face painting, adventure playgrounds, café and ample parking. Current thinking is a home page that will contain links to four separate pages, information about me and a blog from my Chatterbox and Chirpline feeds, one page for two running events being held at Fern Cottage, Marlow Wood (www.woodlandtrustees.example/ferncottage) in October and December and another page for an event at Edith Vane Wood (www.woodlandtrustees.example/edithvane) in November. The third page will be information on the different running buggies available and how people can come and view them at each event and try them out on the course and if they like it they can purchase that buggy for a 10% discount of the RRP. They will need to email me to reserve a buggy for use at the event. The forth page will be information on myself ('About Me' and the details from my other website can be used at this stage). There will be a link from each event page to allow people to enter that particular race online from an external website (links to follow). My current website is an online shop selling running buggies (www.pramdash.co.uk).

I'm also looking for the website to be published (access to cPanel will be given to allow this).

Attached is my current logo (this will be replaced by a new one currently being designed but is nearly identical) so will be replaced before the website goes live. Also attached are a couple of photos to give an idea on running with a buggy and the different types of areas being used. One of the pictures is the lineup of running buggies so could be used on the third page as it was taken at one of the event forests. Also attached are two logos for the Woodland Trustees that should be on the home page.

Alongside the website I'm also looking for two flyers to be designed to showcase each running event (to be used on Social Media and public locations such as cafes, nurseries, running clubs, gyms). One flyer for Fern Cottage Marlow Wood event on the 1st October 2017 and the second flyer for the Edith Vane Wood event on the 5th November 2017. Both these flyers will be a separate project and therefore attract additional payment for each. Will look to offer this work to the winning designer.

Target Market(s)

Families

Industry/Entity Type

Events

Number of Pages Required

5+ page

Font styles to use
Sans Serif

Colors

Designer to choose colors to be used in the design.

Requirements
Must have
• Clear and precise information that each buggy running event is family orientated, on an off-road course that has been carefully planned to be used by a buggy. Different page to highlight the event (i've taken a video of each course so people can see what the terrain is like), course map, course distance, hill profile, timings for the day, travel directions, course dates in 2017 and 2018.
• I'm also looking for the website to be published (access to cPanel will be given to allow this).
• Countdown timer to the next event.
Nice to have
• Map of the UK with the locations highlighted (with a link to the event page). More locations to follow during the rest of 2017.
Should not have
• A lot of writing in small font

```html
<!DOCTYPE html>
<html lang="en">
<head>
<meta charset="utf-8">
<title>Pram Dash Days</title>
<link href="https://fonts.googleapis.com/css2?family=Open+Sans:wght@300;400;600;700;800&display=swap" rel="stylesheet">
<style>
:root{
  --orange:#f0a04b;
  --orange-dark:#e8892e;
  --blue:#4a9fd0;
  --grey-text:#8a8a8a;
  --body-text:#555;
  --light-bg:#f3f3f3;
  --green-badge:#7cc242;
  --map-green:#9cab7b;
  --footer:#3a3a3a;
  --footer-deep:#2b2b2b;
  --white:#fff;
}
*{box-sizing:border-box;margin:0;padding:0}
html,body{width:1200px;height:2671px;overflow:hidden}
body{font-family:"Open Sans",Arial,sans-serif;background:var(--white);position:relative;color:var(--body-text)}
.abs{position:absolute}
/* top bar */
.top-bar{left:0;top:0;width:1200px;height:28px;background:var(--orange);color:var(--white);font-size:11px;font-weight:700;display:flex;justify-content:flex-end;align-items:center;gap:16px;padding-right:240px}
.top-bar .social{font-weight:600;font-size:10px;opacity:.95}
/* header */
.site-header{left:0;top:28px;width:1200px;height:76px;background:var(--white)}
.brand{position:absolute;left:244px;top:16px;display:flex;align-items:center;gap:10px;font-weight:700;font-size:22px;color:var(--orange)}
.brand .dot{width:42px;height:42px;border-radius:50%;background:var(--orange)}
.nav{position:absolute;left:530px;top:24px;display:flex;gap:14px;align-items:center;font-weight:700;font-size:15px;color:#7a7a7a}
.nav .active{color:var(--orange);position:relative}
.nav .active:after{content:"";position:absolute;left:0;right:0;top:46px;height:3px;background:var(--orange)}
.nav .register{background:#9a9a9a;color:var(--white);font-size:11px;padding:6px 24px 6px 9px;border-radius:2px;position:relative}
.nav .register:after{content:"›";position:absolute;right:6px;top:2px;font-size:15px}
/* hero */
.hero{left:0;top:104px;width:1200px;height:532px;background:#f5f5f4;overflow:hidden}
.hero-photo{position:absolute;left:520px;top:0;width:680px;height:532px;background:linear-gradient(100deg,rgba(245,245,244,1) 0%,rgba(200,215,150,.5) 18%,#9bb85a 40%,#6f8f3b 65%,#c9d7a0 100%)}
.hero-title{position:absolute;left:101px;top:48px;font-size:58px;line-height:70px;font-weight:300;color:var(--orange);letter-spacing:.5px}
.hero-title b{font-weight:700}
.hero-text{position:absolute;left:104px;top:222px;width:440px;font-size:15px;line-height:23px;font-weight:700;color:#a0a0a0}
.hero-text .more{color:#8cba2f}
.partner-badge{position:absolute;left:101px;top:350px;width:237px;height:150px;background:var(--green-badge);border-radius:6px 10px 4px 12px}
.discover{position:absolute;left:540px;top:362px;width:140px;text-align:center;font-size:15px;font-weight:700;color:#a0a0a0}
.discover svg{display:block;margin:0 auto 12px}
/* about */
.about{left:0;top:636px;width:1200px;height:325px;background:var(--light-bg)}
.section-title{position:absolute;left:0;width:1200px;text-align:center;font-size:28px;font-weight:700;color:var(--orange);letter-spacing:1px}
.about-photo{position:absolute;left:110px;top:85px;width:167px;height:167px;border-radius:50%;border:6px solid var(--orange);background:radial-gradient(circle at 50% 40%,#c98a5a,#7d5a3b 60%,#3f5a2d)}
.about-text{position:absolute;left:320px;top:100px;width:780px;font-size:19px;line-height:30px;font-weight:700;color:#7a7a7a}
.about-more{position:absolute;right:0;top:208px;width:120px;height:117px}
.about-more span{position:absolute;right:10px;top:48px;font-size:17px;font-weight:800;color:var(--blue);text-align:center;line-height:22px}
/* events */
.events{left:0;top:961px;width:1200px;height:939px;background:var(--white)}
.event-card{position:absolute;background:linear-gradient(180deg,#6b5a2a,#a7853f 45%,#5d4a20)}
.event-card.misty{background:linear-gradient(180deg,#1f4a5a,#4f7f85 50%,#1a3a45)}
.event-card .frame{position:absolute;left:22px;top:22px;right:22px;bottom:22px;border:4px solid var(--white)}
.event-card .place{position:absolute;left:0;right:0;top:38px;text-align:center;color:var(--white);font-weight:700;font-size:25px;line-height:32px}
.event-card .date{position:absolute;left:42px;display:flex;align-items:flex-end;color:var(--orange);font-weight:800;line-height:1}
.event-card .date .num{font-size:72px;line-height:60px}
.event-card .date .rest{display:flex;flex-direction:column;margin-left:2px;padding-bottom:2px}
.event-card .date .sfx{font-size:28px;line-height:26px}
.event-card .date .month{font-size:30px;line-height:30px;margin-left:-4px}
.event-card .details{position:absolute;left:0;right:0;text-align:center;color:var(--white);font-weight:700;font-size:22px;text-decoration:underline}
.countdown{position:absolute;display:flex;gap:12px}
.cd-group{position:relative;display:flex;gap:3px}
.cd-group .label{position:absolute;top:-20px;left:0;right:0;text-align:center;font-size:10px;font-weight:600;color:#444}
.tile{width:38px;height:50px;background:linear-gradient(#fafafa,#e4e4e4);border:2px solid #bbb;border-radius:4px;display:flex;align-items:center;justify-content:center;font-size:34px;font-weight:700;color:#333;box-shadow:0 1px 2px rgba(0,0,0,.25)}
.desc-head{position:absolute;font-size:17px;font-weight:700;color:var(--orange)}
.desc-text{position:absolute;font-size:14.5px;line-height:28px;color:#555}
.desc-text .more{color:var(--orange)}
.profile{position:absolute;width:600px;height:170px}
.stop{position:absolute;width:88px;height:88px;border-radius:50%;background:var(--white);border:3px solid #f6c48e;box-shadow:0 0 0 4px #fbe2c6 inset}
.stop .core{position:absolute;left:8px;top:8px;width:66px;height:66px;border-radius:50%;background:var(--orange);color:var(--white);font-size:13px;font-weight:700;text-align:center;padding-top:12px}
.stop svg{display:block;margin:0 auto 2px}
.tag{position:absolute;font-size:12px;font-weight:700;color:var(--blue)}
.leader{position:absolute;left:0;top:0}
/* map */
.map{left:0;top:1900px;width:1200px;height:423px;background:var(--map-green);text-align:center;color:var(--white)}
.map h2{position:absolute;left:0;width:1200px;top:122px;font-size:36px;font-weight:800;letter-spacing:1.5px}
.map h3{position:absolute;left:0;width:1200px;top:176px;font-size:34px;font-weight:700;letter-spacing:1px}
.map .view{position:absolute;left:520px;top:247px;width:165px;height:40px;border:3px solid var(--white);font-size:20px;font-weight:700;line-height:34px}
/* footer */
.site-footer{left:0;top:2323px;width:1200px;height:309px;background:var(--footer);color:#ddd}
.foot-brand{position:absolute;left:157px;top:30px;display:flex;align-items:center;gap:10px;font-size:22px;font-weight:700;color:var(--orange)}
.foot-brand .dot{width:46px;height:46px;border-radius:50%;background:var(--orange)}
.foot-about{position:absolute;left:157px;top:116px;width:200px;font-size:12px;line-height:19px;font-weight:700;color:#cfcfcf}
.foot-social{position:absolute;left:157px;top:222px;display:flex;gap:14px;font-size:12px;font-weight:700;color:var(--white)}
.foot-head{position:absolute;top:27px;font-size:19px;font-weight:700;color:var(--white)}
.fast-links{position:absolute;left:530px;top:66px;width:140px;list-style:none}
.fast-links li{height:36px;line-height:34px;border-bottom:1px solid #4c4c4c;font-size:15px;font-weight:700;color:#ddd}
.fast-links li.current{color:#666}
.chirp-box{position:absolute;left:853px;top:71px;width:176px;height:210px;background:var(--white);border-radius:3px;color:#333;font-size:8px;padding:6px}
.chirp-box .bar{display:flex;justify-content:space-between;font-weight:700;font-size:10px;border-bottom:1px solid #ddd;padding-bottom:4px}
.chirp-box .follow{font-size:7px;border:1px solid #aaa;padding:1px 3px;border-radius:2px}
.chirp{display:flex;gap:5px;padding:6px 0;border-bottom:1px solid #eee;line-height:10px}
.chirp .sq{width:18px;height:18px;background:var(--orange);flex:none}
.chirp b{display:block}
.chirp .meta{color:#888}
.chirp-box .foot{position:absolute;bottom:4px;left:6px;color:#888;font-size:7px}
.copy-bar{left:0;top:2632px;width:1200px;height:39px;background:var(--footer-deep);color:#777;font-size:12px;text-align:center;line-height:39px}
</style>
</head>
<body>

<div class="abs top-bar">
  <span>Call : 07700 900123</span><span>Mail : hello@pramdashdays.co.uk</span>
  <span class="social">Chatterbox · Snapbook · Chirpline</span>
</div>

<header class="abs site-header">
  <div class="brand"><span class="dot"></span>pramdashdays.co.uk</div>
  <nav class="nav">
    <span class="active">Home</span><span>Events</span><span>Our Product</span><span>About Us</span>
    <span class="register">Register Now</span>
  </nav>
</header>

<section class="abs hero">
  <div class="hero-photo" role="img" aria-label="Photo of a woman running with a child in a jogging buggy on a sunny woodland path"></div>
  <h1 class="hero-title">THE <b>PRAM</b><br><b>DASH</b> DAYS</h1>
  <p class="hero-text">The running events are aimed at getting kids to experience the outdoors whilst parents can keep fit "Fitness for Familes" therefore allowing families to be more active together. <span class="more">READ MORE</span></p>
  <div class="partner-badge" role="img" aria-label="Woodland Trustees partner badge"></div>
  <div class="discover">
    <svg width="90" height="110" viewBox="0 0 90 110" fill="none" stroke="#f0a04b" stroke-width="2.5">
      <path d="M14 72 C4 44 22 8 46 10 C66 12 74 40 74 92" stroke-dasharray="9 6"/>
      <path d="M66 94 L74 106 L82 94"/>
    </svg>
    Discover more
  </div>
</section>

<section class="abs about">
  <h2 class="section-title" style="top:24px">ABOUT US</h2>
  <div class="about-photo" role="img" aria-label="Portrait of the organiser holding his young daughter outdoors"></div>
  <p class="about-text">I started running in my early teenage years competing in both road and cross country races and became involved in orienteering when I began my Young Pathfinder award. With my running background I was able to compete at a national level and was fortunate enough to attend Great Britain training camps.</p>
  <div class="about-more">
    <svg width="120" height="117" viewBox="0 0 120 117" fill="none" stroke="#f0a04b" stroke-width="5"><path d="M4 117 C4 50 50 8 120 4"/></svg>
    <span>READ<br>MORE</span>
  </div>
</section>

<section class="abs events">
  <h2 class="section-title" style="top:22px">EVENTS</h2>

  <div class="event-card" style="left:130px;top:79px;width:324px;height:286px" role="img" aria-label="Sunlit forest clearing at Fern Cottage, Marlow Wood">
    <div class="frame"></div>
    <div class="place">Fern Cottage<br>Marlow Wood</div>
    <div class="date" style="top:132px"><span class="num">1</span><span class="rest"><span class="sfx">st</span><span class="month">OCTOBER</span></span></div>
    <div class="details" style="top:212px">View Details</div>
  </div>
  <div class="countdown" style="left:137px;top:415px">
    <div class="cd-group"><span class="label">DAYS</span><div class="tile">4</div><div class="tile">9</div></div>
    <div class="cd-group"><span class="label">HOURS</span><div class="tile">1</div><div class="tile">3</div></div>
    <div class="cd-group"><span class="label">MINUTES</span><div class="tile">0</div><div class="tile">3</div></div>
  </div>

  <div class="desc-head" style="left:502px;top:95px">Description :</div>
  <p class="desc-text" style="left:502px;top:124px;width:540px">At the Fern Cottage, Marlow Wood (www.woodlandtrustees.example/ferncottage) running event to be held on the 1st October 2017 December 2017, we will be using Oak Lodge as the registration centre which is a separate building, set in it's own grounds and is a 3 minute walk from the Fern Cottage. <span class="more">READ MORE</span></p>
  <div class="desc-head" style="left:502px;top:300px">Course profile :</div>

  <div class="profile" style="left:502px;top:322px">
    <svg class="leader" width="600" height="170" fill="none" stroke="#4a9fd0" stroke-width="1">
      <path d="M0 138 H62 L88 108"/><path d="M170 148 L196 114"/><path d="M336 148 L314 114"/><path d="M560 18 H490 L472 38"/>
    </svg>
    <div class="stop" style="left:65px;top:25px"><div class="core"><svg width="18" height="20" viewBox="0 0 18 20" fill="none" stroke="#fff" stroke-width="1.5"><path d="M9 2v16M3 4h11l2 2-2 2H3z"/></svg>West</div></div>
    <div class="stop" style="left:179px;top:25px"><div class="core"><svg width="22" height="20" viewBox="0 0 22 20" fill="none" stroke="#fff" stroke-width="1.5"><path d="M1 18L8 6l4 6 3-4 6 10z"/></svg>200M</div></div>
    <div class="stop" style="left:282px;top:25px"><div class="core"><svg width="20" height="20" viewBox="0 0 20 20" fill="none" stroke="#fff" stroke-width="1.5"><circle cx="10" cy="10" r="8"/><path d="M10 5v5l3 2"/></svg>8-10 AM</div></div>
    <div class="stop" style="left:389px;top:25px"><div class="core"><svg width="20" height="20" viewBox="0 0 20 20" fill="none" stroke="#fff" stroke-width="1.5"><path d="M10 18s-6-6-6-10a6 6 0 0112 0c0 4-6 10-6 10z"/><circle cx="10" cy="8" r="2"/></svg>3 Miles</div></div>
    <span class="tag" style="left:0;top:120px">Direction</span>
    <span class="tag" style="left:112px;top:142px">The Hill</span>
    <span class="tag" style="left:340px;top:142px">Timing</span>
    <span class="tag" style="left:506px;top:0">Distance</span>
  </div>

  <div class="desc-head" style="left:130px;top:520px">Description :</div>
  <p class="desc-text" style="left:130px;top:550px;width:560px">At the Edith Vane Wood (www.woodlandtrustees.example/edithvane) running event to be held on the 5thNovember, we will be using an undercover area for the registration centre which will be right next to the start and finish. The main café and toilets are less than a minute walk away. <span class="more">READ MORE</span></p>
  <div class="desc-head" style="left:130px;top:690px">Course profile :</div>

  <div class="profile" style="left:130px;top:716px">
    <svg class="leader" width="600" height="170" fill="none" stroke="#4a9fd0" stroke-width="1">
      <path d="M0 138 H66 L94 110"/><path d="M170 148 L196 116"/><path d="M336 148 L314 116"/><path d="M560 18 H490 L472 40"/>
    </svg>
    <div class="stop" style="left:72px;top:27px"><div class="core"><svg width="18" height="20" viewBox="0 0 18 20" fill="none" stroke="#fff" stroke-width="1.5"><path d="M9 2v16M3 4h11l2 2-2 2H3z"/></svg>West</div></div>
    <div class="stop" style="left:177px;top:27px"><div class="core"><svg width="22" height="20" viewBox="0 0 22 20" fill="none" stroke="#fff" stroke-width="1.5"><path d="M1 18L8 6l4 6 3-4 6 10z"/></svg>200M</div></div>
    <div class="stop" style="left:282px;top:27px"><div class="core"><svg width="20" height="20" viewBox="0 0 20 20" fill="none" stroke="#fff" stroke-width="1.5"><circle cx="10" cy="10" r="8"/><path d="M10 5v5l3 2"/></svg>8-10 AM</div></div>
    <div class="stop" style="left:387px;top:27px"><div class="core"><svg width="20" height="20" viewBox="0 0 20 20" fill="none" stroke="#fff" stroke-width="1.5"><path d="M10 18s-6-6-6-10a6 6 0 0112 0c0 4-6 10-6 10z"/><circle cx="10" cy="8" r="2"/></svg>3 Miles</div></div>
    <span class="tag" style="left:0;top:120px">Direction</span>
    <span class="tag" style="left:112px;top:142px">The Hill</span>
    <span class="tag" style="left:340px;top:142px">Timing</span>
    <span class="tag" style="left:506px;top:0">Distance</span>
  </div>

  <div class="event-card misty" style="left:748px;top:501px;width:317px;height:283px" role="img" aria-label="Misty woodland path at Edith Vane Wood">
    <div class="frame"></div>
    <div class="place" style="top:30px">Edith Vane<br>Wood</div>
    <div class="date" style="top:126px"><span class="num">5</span><span class="rest"><span class="sfx">th</span><span class="month">NOVEMBER</span></span></div>
    <div class="details" style="top:208px">View Details</div>
  </div>
  <div class="countdown" style="left:755px;top:835px">
    <div class="cd-group"><span class="label">DAYS</span><div class="tile">8</div><div class="tile">4</div></div>
    <div class="cd-group"><span class="label">HOURS</span><div class="tile">1</div><div class="tile">3</div></div>
    <div class="cd-group"><span class="label">MINUTES</span><div class="tile">1</div><div class="tile">1</div></div>
  </div>
</section>

<section class="abs map" role="img" aria-label="Street map around Fern Cottage, Marlow Wood">
  <h2>RUNNING EVENT MAP</h2>
  <h3>The Fern Cottage, Marlow Wood</h3>
  <div class="view">Click to view</div>
</section>

<footer class="abs site-footer">
  <div class="foot-brand"><span class="dot"></span>pramdashdays.co.uk</div>
  <p class="foot-about">Pram Dash Days is a brand new concept developed by Dan Hollis, a competitive runner and father of a tireless daughter.</p>
  <div class="foot-social"><span>Chatterbox</span><span>Snapbook</span><span>Chirpline</span></div>

  <div class="foot-head" style="left:530px">Fast Links</div>
  <ul class="fast-links">
    <li class="current">Home</li><li>Events</li><li>Our Product</li><li>About Us</li><li>Search</li>
  </ul>

  <div class="foot-head" style="left:853px">Our Chirpline</div>
  <div class="chirp-box">
    <div class="bar"><span>Chirps</span><span class="follow">Follow @PramDashDays</span></div>
    <div class="chirp"><span class="sq"></span><div><b>Pram Dash Days</b><span class="meta">@PramDashDays · 16 Nov</span><br>Entries now open for Fern Cottage.</div></div>
    <div class="chirp"><span class="sq"></span><div><b>Pram Dash Days</b><span class="meta">@PramDashDays · 16 Nov</span><br>Course video is up, take a look at the woodland trails.</div></div>
    <div class="chirp"><span class="sq"></span><div><b>Pram Dash Days</b><span class="meta">@PramDashDays · 16 Nov</span></div></div>
    <span class="foot">Chirp to @PramDashDays</span>
  </div>
</footer>

<div class="abs copy-bar">Copyright © 2017 – Pram Dash Days – All Rights Reserved</div>

</body>
</html>
```